Legal consulting business needs flyer

Legal consulting firm that helps state associations provide CLE classes to personal injury attorney members at no cost to the association. The state Association can offer the class for free or charge the normal CLE amount and all funds remain with the association. We teach witness preparation, trial presentation, and preparing cases for trial.
We are often asked how we're able to do this for no cost and it boils down to: trust and credibility. Ultimately, we teach information the attorney can use immediately but in the future, if they need more detailed help on their case, they will contact us for a source of knowledge for preparing a case for trial.
1-hour CLE class to an 8-hour in-person CLE seminar.

I have attached the description of the classes and bios of the instructors.

A flyer that the executive or committee chair could read and understand what we do and see the benefit of bringing us aboard for seminars for their members while the association also benefits as they keep all funding that is made during our seminar.

Target Market(s)

Justice Associations

Industry/Entity Type

Plaintiff injury attorney associations

Requirements
Must have
• With an emphasis on providing classes to state justice associations.

```html
<!DOCTYPE html>
<html lang="en">
<head>
<meta charset="utf-8">
<title>Verdict Frame – CLE Course Guide</title>
<link rel="stylesheet" href="https://fonts.googleapis.com/css2?family=Rubik:wght@500;600&family=Work+Sans:wght@300;400;500;600&display=swap">
<style>
:root{
  --navy:#1b1f3b;
  --tan:#c0ad7e;
  --ink:#1b1f3b;
  --paper:#ececec;
  --text-light:#e6e4dc;
  --line:#3a3f5e;
}
*{margin:0;padding:0;box-sizing:border-box}
html,body{width:1200px;height:1200px;overflow:hidden}
body{background:var(--paper);font-family:"Work Sans",Arial,sans-serif;color:var(--text-light);position:relative}
.page{position:absolute;width:414px;height:585px;background:var(--navy);overflow:hidden}
.page--cover{left:181px;top:10px}
.page--consultants{left:605px;top:10px}
.page--courses-a{left:181px;top:605px}
.page--courses-b{left:605px;top:605px}
.abs{position:absolute}

.brand{display:flex;align-items:center;gap:6px;font-family:"Rubik",sans-serif;font-weight:600;color:#fff;letter-spacing:.2px}
.brand__mark{width:14px;height:14px;background:var(--tan)}

.tag{position:absolute;background:var(--tan);color:var(--ink);font-family:"Rubik",sans-serif;font-weight:500;display:flex;align-items:center;justify-content:center}

/* cover */
.cover-brand{left:30px;top:28px;font-size:13px}
.headline{left:34px;top:80px;font-weight:300;font-size:24px;line-height:30px;color:#fff}
.headline strong{font-family:"Rubik",sans-serif;font-weight:600;color:var(--tan)}
.subline{left:34px;top:190px;font-size:11px;font-weight:300;color:#fff}
.cover-tag{left:33px;top:222px;width:81px;height:21px;font-size:9px}
.cover-band{left:0;top:454px;width:414px;height:131px;background:var(--tan)}
.cover-frame{left:33px;top:277px;width:390px;height:215px;border:1px solid #b7b6b6}
.cover-photo{left:46px;top:293px;width:368px;height:215px;background:linear-gradient(135deg,#3b3530 0%,#4a4741 40%,#26262c 100%)}
.cover-title{left:34px;top:528px;font-family:"Rubik",sans-serif;font-weight:600;font-size:22px;color:var(--ink)}
.contact{font-size:7.5px;color:var(--ink)}
.cover-contact{left:34px;top:557px}

/* consultants */
.consult-tag{left:27px;top:20px;width:92px;height:21px;font-size:11px}
.consult-rule{left:119px;top:30px;width:295px;height:1px;background:var(--line)}
.portrait{position:absolute;left:26px;width:70px;height:70px;border-radius:50%;border:1px solid #8a8aa0;display:flex;align-items:center;justify-content:center}
.portrait span{width:60px;height:60px;border-radius:50%;background:radial-gradient(circle at 50% 40%,#a9a29a,#4c5a55)}
.bio{position:absolute;left:108px;width:280px;font-size:6.6px;line-height:9.7px;font-weight:300;color:var(--text-light)}
.bio b{color:#fff;font-weight:600}
.quote{left:29px;top:426px;width:357px;height:105px;background:var(--tan);color:var(--ink);padding:12px 14px 0 37px}
.quote__icon{position:absolute;left:10px;top:14px}
.quote__title{font-family:"Rubik",sans-serif;font-weight:500;font-size:10px;margin-bottom:5px}
.quote__body{font-size:6.6px;line-height:9px}
.quote__source{display:flex;align-items:center;gap:4px;margin-top:8px;font-size:7px;font-weight:500}
.quote__source i{width:7px;height:7px;border-radius:50%;background:var(--ink);display:block}
.consult-rule-foot{left:30px;top:543px;width:354px;height:1px;background:var(--line)}
.consult-contact{left:30px;top:557px;color:var(--text-light)}
.consult-brand{left:288px;top:553px;font-size:9px}
.consult-brand .brand__mark{width:10px;height:10px}

/* course pages */
.course-tag{width:50px;height:13px;font-size:7px}
.course-title{font-size:10px;line-height:12px;color:#fff}
.course-title b{font-family:"Rubik",sans-serif;font-weight:500}
.course-title span{font-weight:300}
.course-body{font-size:6.8px;line-height:9px;color:var(--text-light)}
.course-body p+p{margin-top:9px}
.checks{list-style:none;font-size:6.8px;line-height:9px;color:var(--text-light)}
.checks li{position:relative;padding:0 0 5px 12px;margin-bottom:6px;border-bottom:1px solid var(--line)}
.checks li:last-child{border-bottom:none}
.checks svg{position:absolute;left:0;top:1px}
.photo{position:absolute}
.foot{left:0;top:557px;width:414px;height:28px;background:var(--tan);display:flex;align-items:center;justify-content:center}
</style>
</head>
<body>

<section class="page page--cover">
  <div class="abs brand cover-brand"><span class="brand__mark"></span>VERDICT FRAME</div>
  <h1 class="abs headline">The #1 Plaintiff's<br><strong>Litigation Strategy Program</strong><br>in the country</h1>
  <p class="abs subline">1 to 8-Hour CLE Seminars at no cost to the Association</p>
  <div class="tag cover-tag">COURSE GUIDE</div>
  <div class="abs cover-band"></div>
  <div class="abs cover-frame"></div>
  <div class="abs cover-photo" role="img" aria-label="Photo of attorneys in suits talking in a law office with a flag and bookshelves"></div>
  <h2 class="abs cover-title">Trust &amp; Credibility</h2>
  <p class="abs contact cover-contact">verdictframe.com | info@verdictframe.com | 555-014-2288</p>
</section>

<section class="page page--consultants">
  <div class="tag consult-tag">CONSULTANTS</div>
  <div class="abs consult-rule"></div>

  <div class="portrait" style="top:69px" role="img" aria-label="Portrait of consultant Marco D. Ruiz"><span></span></div>
  <p class="bio" style="top:64px"><b>Marco D. Ruiz</b> is the founder of Verdict Frame with over 100 civil and criminal cases tried to jury. Marco has accomplished extraordinary results in cases with contested liability, disputed liability and complex medical issues in the tens of millions of dollars. Specializing in brain injuries and complex medicine, Marco has worked as co-counsel and consultant alongside some of the most prestigious trial lawyers in the business. His knowledge of persuasion and cutting-edge trial strategy has made him a valuable addition to trial teams across the country in both state and federal courts. He has taught for the Courtroom Craft College and lectured in the country's biggest forums including the Harborfront seminar, WCTLA, National Justice Alliance, and the National Litigators Guild.</p>

  <div class="portrait" style="top:167px" role="img" aria-label="Portrait of consultant Thomas Avery"><span></span></div>
  <p class="bio" style="top:181px"><b>Thomas Avery</b> is both a personal injury lawyer and a trial consultant for all types of catastrophic personal injury cases. Thomas has notable consulting verdicts, including in July 2021, Thomas won a $325,000 verdict in a conservative county, on a contested red light, he-said-she-said case, with less than $40k in past medical bills and a last offer of approximately $19k.</p>

  <div class="portrait" style="top:251px" role="img" aria-label="Portrait of consultant Nadia Voss"><span></span></div>
  <p class="bio" style="top:251px"><b>Nadia Voss</b> for more than 20 years, has represented Plaintiffs in a wide array of complex personal injury matters. She has successfully prevailed in claims involving governmental entities, hospitals, multi-national corporations, heavy equipment and transportation companies, and mainline insurance carriers. Nadia has presented at the National Litigators Guild, National Justice Alliance "Spring Advocacy Summit," Coastal Justice Association, and Plains Trial Lawyers Association to name a few. She is a member of the Executive Board of the Desert State Trial Lawyers Association and the 2021-2022 President of the Desert State Association for Justice.</p>

  <div class="portrait" style="top:335px" role="img" aria-label="Portrait of consultant Owen Pratt"><span></span></div>
  <p class="bio" style="top:345px"><b>Owen Pratt's</b> first exposure to great trial lawyer skills was while working for famed criminal defense attorney Leon Hart in Miami, Florida. After turning his focus to Civil Plaintiff work, he graduated from the Summit Trial College, having been voted class representative and serving on the Vanguard Board for three years. Owen was a founding instructor of Open Gate Method and Verdict Frame, where he has taught, presented and consulted across the country for several years.</p>

  <div class="abs quote">
    <svg class="quote__icon" width="20" height="14" viewBox="0 0 20 14" aria-hidden="true"><path d="M0 0h8v8l-3 6H1l3-6H0z M11 0h8v8l-3 6h-4l3-6h-4z" fill="#1b1f3b"/></svg>
    <p class="quote__title">Working with Verdict Frame has been a pleasure.</p>
    <p class="quote__body">Verdict Frame provides informative, helpful content that our seminar attendees love. Since we began working with them to provide programs to our national series of programs, our attendees have overwhelmingly rated the programs positively and asked for additional follow up presentations from the speakers. Marco, Thomas, and Nadia are incredibly knowledgeable and engaging speakers, and they provide valuable content and materials.</p>
    <p class="quote__source"><i></i>eventhall</p>
  </div>

  <div class="abs consult-rule-foot"></div>
  <p class="abs contact consult-contact">verdictframe.com | info@verdictframe.com | 555-014-2288</p>
  <div class="abs brand consult-brand"><span class="brand__mark"></span>VERDICT FRAME</div>
</section>

<section class="page page--courses-a">
  <div class="tag course-tag" style="left:21px;top:32px">COURSE #1</div>
  <h3 class="abs course-title" style="left:21px;top:54px"><b>Advanced Witness Preparation:</b><br><span>Help your personal injury client tell their story</span></h3>
  <div class="abs course-body" style="left:23px;top:87px;width:222px">
    <p>Learn how to prepare your client to be a compelling witness at deposition and trial using state-of-the-art neurological science developed from advanced therapeutic techniques. Help your client tell the story of what happened so the jury sees, hears, and feels the depths of what the defendant did.</p>
    <p>We will teach you how to obtain the story of the injury from your client and how to help your client present the story in its purest form during direct and cross-examination testimony. The Verdict Frame Advanced Witness Preparation system will provide you with accessible strategies to transform your client into a master teller witness of their story.</p>
  </div>
  <ul class="abs checks" style="left:23px;top:208px;width:236px">
    <li><svg width="8" height="7" viewBox="0 0 8 7"><path d="M1 3.5l2 2L7 1" stroke="#c0ad7e" stroke-width="1.6" fill="none"/></svg>Turn your client into a compelling witness at deposition and trial</li>
    <li><svg width="8" height="7" viewBox="0 0 8 7"><path d="M1 3.5l2 2L7 1" stroke="#c0ad7e" stroke-width="1.6" fill="none"/></svg>Prepare your client using state-of-the-art neurological science developed from advanced therapeutic techniques</li>
    <li><svg width="8" height="7" viewBox="0 0 8 7"><path d="M1 3.5l2 2L7 1" stroke="#c0ad7e" stroke-width="1.6" fill="none"/></svg>Help your client tell their story so the jury sees, hears, and feels the depths of what the defendant did.</li>
  </ul>
  <div class="photo" style="left:265px;top:0;width:132px;height:287px;background:linear-gradient(180deg,#4a2e22 0%,#5b3a2a 45%,#2b2a30 100%)" role="img" aria-label="Photo of an attorney in a suit explaining at a conference table"></div>

  <div class="photo" style="left:20px;top:303px;width:120px;height:254px;background:linear-gradient(160deg,#2a2422 0%,#3c3632 50%,#1e1c1f 100%)" role="img" aria-label="Photo of two lawyers reviewing documents at a desk beside a flag"></div>
  <div class="tag course-tag" style="left:161px;top:315px">COURSE #2</div>
  <h3 class="abs course-title" style="left:161px;top:337px"><b>Structuring your Plaintiff Damages Case:</b><br><span>Turn ordinary into extraordinary</span></h3>
  <div class="abs course-body" style="left:162px;top:371px;width:223px">
    <p>Turn ordinary into extraordinary by structuring your plaintiff injury case for voir dire, opening statement, and closing argument so the jury can see, hear, and feel the truth of what the defense did to your client. Learn how to make complex medical causation issues easily understandable for the jury and get the most out of your client's story.</p>
  </div>
  <ul class="abs checks" style="left:162px;top:442px;width:223px">
    <li><svg width="8" height="7" viewBox="0 0 8 7"><path d="M1 3.5l2 2L7 1" stroke="#c0ad7e" stroke-width="1.6" fill="none"/></svg>Focus the jury on the defendant</li>
    <li><svg width="8" height="7" viewBox="0 0 8 7"><path d="M1 3.5l2 2L7 1" stroke="#c0ad7e" stroke-width="1.6" fill="none"/></svg>Identify what the defense will say and how they will say it</li>
    <li><svg width="8" height="7" viewBox="0 0 8 7"><path d="M1 3.5l2 2L7 1" stroke="#c0ad7e" stroke-width="1.6" fill="none"/></svg>Use advanced linguistics to speak to the jury on a deeper level</li>
    <li><svg width="8" height="7" viewBox="0 0 8 7"><path d="M1 3.5l2 2L7 1" stroke="#c0ad7e" stroke-width="1.6" fill="none"/></svg>How to present complex medical causation in opening</li>
  </ul>
  <div class="abs foot"><p class="contact">verdictframe.com | info@verdictframe.com | 555-014-2288</p></div>
</section>

<section class="page page--courses-b">
  <div class="tag course-tag" style="left:24px;top:32px">COURSE #3</div>
  <h3 class="abs course-title" style="left:24px;top:54px"><b>Bring Your Client's Story to Life:</b><br><span>Persuasion and Presentation Skills</span></h3>
  <div class="abs course-body" style="left:25px;top:87px;width:235px">
    <p>A trial is a contest of credibility. Unfortunately, plaintiff trial attorneys are labeled as "ambulance chasers," putting us at a disadvantage in telling our client's story. By learning how to tell the right story in the right way, jurors will be more receptive to your client's position, adopting it as their own based on the way you tell your client's story.</p>
    <p>We will share proven techniques you can implement to become an expert storyteller, allowing the jury to see, hear, and feel your client's story. You already use many of these techniques to some extent. This webinar will teach you how to employ those same techniques in a more structured method that brings to life your client's story and allows the jury to identify with their experience.</p>
  </div>
  <ul class="abs checks" style="left:25px;top:210px;width:236px">
    <li><svg width="8" height="7" viewBox="0 0 8 7"><path d="M1 3.5l2 2L7 1" stroke="#c0ad7e" stroke-width="1.6" fill="none"/></svg>Tell the right story in the right way so jurors are receptive to your client's position</li>
    <li><svg width="8" height="7" viewBox="0 0 8 7"><path d="M1 3.5l2 2L7 1" stroke="#c0ad7e" stroke-width="1.6" fill="none"/></svg>Use images, dialogue and emotion to help the jury see, hear and feel your client's story</li>
    <li><svg width="8" height="7" viewBox="0 0 8 7"><path d="M1 3.5l2 2L7 1" stroke="#c0ad7e" stroke-width="1.6" fill="none"/></svg>Build on techniques you already use to bring your client's story to life</li>
  </ul>
  <div class="photo" style="left:269px;top:0;width:122px;height:287px;background:linear-gradient(180deg,#eeeeec 0%,#d9cdb8 55%,#3a2418 78%,#2a1a12 100%)" role="img" aria-label="Photo of a woman in a camel blazer reading a law book"></div>

  <div class="photo" style="left:24px;top:303px;width:120px;height:254px;background:linear-gradient(170deg,#4c4844 0%,#3a3430 55%,#241a14 100%)" role="img" aria-label="Photo of two men in suits shaking hands in an office"></div>
  <div class="tag course-tag" style="left:163px;top:302px">COURSE #4</div>
  <h3 class="abs course-title" style="left:163px;top:325px"><b>Dynamics of Expert</b> <span>Witness Protection</span></h3>
  <div class="abs course-body" style="left:163px;top:346px;width:226px">
    <p>In this discussion, you will learn step-by-step organization of the expert witness direct exam, the how-to's of structuring cross-examination and tactics to outscore the Defense on re-direct exam to drive the true story of your case and deflect the Defense conjured-up false-narrative.</p>
    <p>Finally, learn how to make complex medical causation issues easily understandable for the jury and cement the true nature of your client's injury and permanent damage.</p>
  </div>
  <ul class="abs checks" style="left:163px;top:443px;width:230px">
    <li><svg width="8" height="7" viewBox="0 0 8 7"><path d="M1 3.5l2 2L7 1" stroke="#c0ad7e" stroke-width="1.6" fill="none"/></svg>Focus the expert's extraordinary knowledge</li>
    <li><svg width="8" height="7" viewBox="0 0 8 7"><path d="M1 3.5l2 2L7 1" stroke="#c0ad7e" stroke-width="1.6" fill="none"/></svg>Identify what the defense will use as attack and how to turn it against them</li>
    <li><svg width="8" height="7" viewBox="0 0 8 7"><path d="M1 3.5l2 2L7 1" stroke="#c0ad7e" stroke-width="1.6" fill="none"/></svg>Use advanced linguistics to help the jury "hear" on a deeper level</li>
    <li><svg width="8" height="7" viewBox="0 0 8 7"><path d="M1 3.5l2 2L7 1" stroke="#c0ad7e" stroke-width="1.6" fill="none"/></svg>Present complex medical causation in easy-to-follow conversational testimony.</li>
  </ul>
  <div class="abs foot"><p class="contact">verdictframe.com | info@verdictframe.com | 555-014-2288</p></div>
</section>

</body>
</html>
```